TR Advisory Business Cards - High End AV / Low Voltage Company

We are low voltage AV company that specializes in high end clients on the residential side and larger businesses on the commercial side. We want something modern, tech looking but also something that is extremely professional looking. We have uploaded our logos and postcards we already have in the field. Along with a picture of one of our wrapped vans. Our website is at www.trvadvisory.example and our primary colors are the orange, green, grey and blue all military color finishes.

We are interesting in the slogans "Pairing You with the Right Technology" or "Leading the Lowcountry in Tech"

Target Market(s)

We focus on 70% Commercial and 30% Residential Customers

Industry/Entity Type

Low Voltage, AV Company

Contact Information for Business Card

Name - Dorian Fairweather, Title - Owner, Office Phone - 555-714-3096, Mobile Phone - 555-802-4173, E-Mail - d@trvadvisory.example, Website: www.trvadvisory.example

Font styles to use
Sans Serif

Requirements
Must have
• Must have Name, Title, Work Phone & Mobile, Website and Logo.
Nice to have
• We want something that will impress our higher end clients with a great logo
Should not have
• Too traditional or plain.

```html
<!DOCTYPE html>
<html lang="en">
<head>
<meta charset="utf-8">
<title>TR Advisory – Business Cards</title>
<link rel="stylesheet" href="https://fonts.googleapis.com/css2?family=Open+Sans:wght@400;600;700&display=swap">
<style>
  :root {
    --backdrop: #dcdcdc;
    --card-light: #f6f6f6;
    --card-dark: #292929;
    --brand-orange: #dd5f32;
    --band-grey: #505050;
    --text-dark: #2b2b2b;
    --text-muted: #555555;
    --divider: #b5b5b5;
    --mark-on-dark: #4a4a4a;
  }
  * { margin: 0; padding: 0; box-sizing: border-box; }
  html, body { width: 1200px; height: 1040px; overflow: hidden; }
  body {
    background: var(--backdrop);
    font-family: "Open Sans", Arial, sans-serif;
    position: relative;
  }
  .card {
    position: absolute;
    border-radius: 16px;
    overflow: hidden;
    box-shadow: 0 4px 10px rgba(0,0,0,0.25);
  }
  .card--front {
    left: 285px; top: 130px; width: 641px; height: 366px;
    background: var(--card-light);
  }
  .card--back {
    left: 284px; top: 568px; width: 646px; height: 368px;
    background: var(--card-dark);
  }
  .brand-name {
    position: absolute;
    font-weight: 700;
    white-space: nowrap;
    letter-spacing: 0.5px;
  }
  .card--front .brand-name {
    left: 200px; top: 182px; transform: translate(-50%, -50%);
    font-size: 30px; color: var(--brand-orange);
  }
  .card--back .brand-name {
    left: 50%; top: 50%; transform: translate(-50%, -50%);
    font-size: 52px; color: var(--mark-on-dark);
  }
  .divider {
    position: absolute; left: 312px; top: 110px;
    width: 1px; height: 150px; background: var(--divider);
  }
  .person { position: absolute; left: 331px; top: 106px; }
  .person__name {
    font-size: 23px; font-weight: 700; color: var(--brand-orange); line-height: 1.2;
  }
  .person__title {
    font-size: 15px; color: var(--text-muted); line-height: 1.3; margin-left: 2px;
  }
  .contacts { list-style: none; margin-top: 18px; }
  .contacts li {
    display: flex; align-items: center; gap: 8px;
    font-size: 15px; color: var(--text-dark); height: 20px;
  }
  .contacts svg { width: 13px; height: 13px; fill: var(--brand-orange); flex: none; }
  .band { position: absolute; bottom: 0; left: 0; width: 100%; height: 18px; }
</style>
</head>
<body>
  <section class="card card--front">
    <span class="brand-name">TR Advisory</span>
    <div class="divider"></div>
    <div class="person">
      <p class="person__name">Dorian Fairweather</p>
      <p class="person__title">Owner</p>
      <ul class="contacts">
        <li><svg viewBox="0 0 16 16"><path d="M3.5 1 6 3.5 4.6 5.6c.9 2 3 4.1 5.8 5.8L12.5 10 15 12.5 13.2 15C6.5 14.3 1.7 9.5 1 2.8z"/></svg>555-714-3096</li>
        <li><svg viewBox="0 0 16 16"><path d="M4 0h8a1 1 0 0 1 1 1v14a1 1 0 0 1-1 1H4a1 1 0 0 1-1-1V1a1 1 0 0 1 1-1zm1 2v10h6V2zm3 11a1 1 0 1 0 0 2 1 1 0 0 0 0-2z"/></svg>555-802-4173</li>
        <li><svg viewBox="0 0 16 16"><path d="M1 4h14v9H1zm1.5 1.2 5.5 4 5.5-4v-.2h-11z"/></svg>d@trvadvisory.example</li>
        <li><svg viewBox="0 0 16 16"><circle cx="8" cy="8" r="7"/><path d="M5 4c2 1 1 3 3 3s1 3 3 2M4 11c1-1 2 0 3 1" stroke="#f6f6f6" stroke-width="1.3" fill="none"/></svg>www.trvadvisory.example</li>
      </ul>
    </div>
    <svg class="band" viewBox="0 0 641 18" preserveAspectRatio="none">
      <polygon points="0,0 419,0 415,18 0,18" fill="var(--brand-orange)"/>
      <polygon points="424,0 641,0 641,18 420,18" fill="var(--band-grey)"/>
    </svg>
  </section>

  <section class="card card--back">
    <span class="brand-name">TR Advisory</span>
  </section>
</body>
</html>
```